Social Media Graphics - Harbor Climb REVISED

Create 6-7 individual social media graphics (square size) to encourage folks to join our online course called:

The Lantern Ledger Plan
How to Launch a Multi-Million Business From Scratch
Sign Up Today!

IMPORTANT: Make the largest and most prominent text on the graphic be: How to Launch a Multi-Million Business From Scratch

For the color scheme of the graphics, let's try a blue color palette; make sure the graphics appeal to both men and women

Make sure each graphic contains 1 of the 3 pics attached (crop pic as needed); and make sure one of the graphics is all TEXT only.

Target Market(s)

men and women looking to start a business

Industry/Entity Type

Entrepreneurship

Colors
0054AA
0677BA
7BADD7
CADEEF
E8F1F8

Requirements
Must have
• All the text and use the 3 pics provided; one graphic can be all text; Simple, modern design that's easy to read

```html
<!DOCTYPE html>
<html lang="en">
<head>
<meta charset="utf-8">
<title>The Lantern Ledger Plan – Social Graphics</title>
<link href="https://fonts.googleapis.com/css2?family=Bebas+Neue&display=swap" rel="stylesheet">
<style>
  :root {
    --canvas-grey: #c4c4c4;
    --royal: #1f3aa8;
    --royal-deep: #14228a;
    --sky: #6f95dc;
    --sky-soft: #a9c2f0;
    --pale: #cadeef;
    --navy-band: #120a5c;
    --ink-dark: #14161f;
    --denim: #1d4f86;
    --title-light: #93a9f0;
    --white: #ffffff;
  }
  * { margin: 0; padding: 0; box-sizing: border-box; }
  html, body {
    width: 1200px; height: 602px; overflow: hidden;
    background: var(--canvas-grey);
  }
  .sheet { position: relative; width: 1200px; height: 602px; }
  .graphic {
    position: absolute; top: 10px; width: 581px; height: 581px; overflow: hidden;
  }
  .graphic--goal { left: 11px;
    background: radial-gradient(circle at 55% 35%, var(--sky-soft) 0%, var(--sky) 30%, var(--royal) 70%, var(--royal-deep) 100%); }
  .graphic--promise { left: 607px;
    background: radial-gradient(circle at 55% 35%, #4f86e6 0%, #2a55d0 45%, var(--royal-deep) 100%); }
  .founders-photo {
    position: absolute; left: 40px; top: 20px; width: 500px; height: 330px;
    border-radius: 90px 90px 0 0;
    background: linear-gradient(90deg, var(--ink-dark) 0%, #232633 50%, var(--denim) 62%, #2a64a0 100%);
    -webkit-mask-image: linear-gradient(180deg, #000 60%, transparent 100%);
            mask-image: linear-gradient(180deg, #000 60%, transparent 100%);
    opacity: .9;
  }
  .headline {
    position: absolute; inset: 0; width: 581px; height: 581px;
    font-family: "Bebas Neue", "Oswald", sans-serif;
  }
  .headline text { fill: var(--white); filter: drop-shadow(0 2px 3px rgba(0,0,0,.45)); }
  .headline .entrepreneurship { fill: var(--title-light); filter: none; }
  .headline .main-title { fill: var(--white); filter: none; }
  .headline .cta-text { fill: var(--navy-band); filter: none; }
  .title-box { fill: var(--navy-band); stroke: #cfd8ff; stroke-width: 1; }
  .course-band { fill: var(--navy-band); }
  .cta-pill { fill: var(--pale); }
</style>
</head>
<body>
<main class="sheet">

  <section class="graphic graphic--goal">
    <div class="founders-photo" role="img" aria-label="Photo of the two course founders, arms crossed and smiling, on a blue sunburst backdrop"></div>
    <svg class="headline" viewBox="0 0 581 581">
      <text x="290" y="40" font-size="28" text-anchor="middle" letter-spacing="3">THE LANTERN LEDGER PLAN</text>
      <text x="290" y="262" font-size="28" text-anchor="middle" letter-spacing="6">SET ASIDE</text>
      <text x="290" y="312" font-size="54" text-anchor="middle">90 DAYS</text>
      <text x="290" y="340" font-size="26" text-anchor="middle" letter-spacing="4">FOR YOUR GOAL.</text>
      <rect class="course-band" x="0" y="352" width="581" height="229"/>
      <text class="main-title" x="290" y="412" font-size="62" text-anchor="middle">HOW TO LAUNCH A</text>
      <text class="main-title" x="290" y="472" font-size="62" text-anchor="middle" textLength="520" lengthAdjust="spacingAndGlyphs">MULTI-MILLION BUSINESS</text>
      <text class="main-title" x="290" y="532" font-size="62" text-anchor="middle">FROM SCRATCH</text>
      <rect class="cta-pill" x="200" y="543" width="181" height="30" rx="15"/>
      <text class="cta-text" x="290" y="566" font-size="22" text-anchor="middle" letter-spacing="1">SIGN UP TODAY!</text>
    </svg>
  </section>

  <section class="graphic graphic--promise">
    <div class="founders-photo" role="img" aria-label="Photo of the two course founders, arms crossed and smiling, on a blue patterned backdrop"></div>
    <svg class="headline" viewBox="0 0 581 581">
      <text x="290" y="40" font-size="28" text-anchor="middle" letter-spacing="3">THE LANTERN LEDGER PLAN</text>
      <text x="290" y="262" font-size="28" text-anchor="middle">BECOME A SUCCESSFUL</text>
      <rect class="title-box" x="150" y="270" width="281" height="38"/>
      <text class="entrepreneurship" x="290" y="301" font-size="34" text-anchor="middle" textLength="260" lengthAdjust="spacingAndGlyphs">ENTREPRENEURSHIP</text>
      <text x="290" y="345" font-size="38" text-anchor="middle">IN 90 DAYS</text>
      <rect class="course-band" x="0" y="352" width="581" height="229"/>
      <text class="main-title" x="290" y="412" font-size="62" text-anchor="middle">HOW TO LAUNCH A</text>
      <text class="main-title" x="290" y="472" font-size="62" text-anchor="middle" textLength="520" lengthAdjust="spacingAndGlyphs">MULTI-MILLION BUSINESS</text>
      <text class="main-title" x="290" y="532" font-size="62" text-anchor="middle">FROM SCRATCH</text>
      <rect class="cta-pill" x="200" y="543" width="181" height="30" rx="15"/>
      <text class="cta-text" x="290" y="566" font-size="22" text-anchor="middle" letter-spacing="1">SIGN UP TODAY!</text>
    </svg>
  </section>

</main>
</body>
</html>
```